Bookkeeping website design

We need a basic site design for wordpress.
We are a bookkeeping business and will need to present a look consistent with the colours and style of the logo.

Target Market(s)

Business owners

Industry/Entity Type

Accounting/Bookkeeping

Coding

Coded - Design and coding required

Number of Pages Required

1 page

```html
<!DOCTYPE html>
<html lang="en">
<head>
<meta charset="utf-8">
<title>Ledgerline Bookkeeping</title>
<link href="https://fonts.googleapis.com/css2?family=Outfit:wght@300;400;500;600;700&display=swap" rel="stylesheet">
<style>
:root{
  --blue:#19b2e3;
  --green:#8dc63f;
  --green-soft:#a6d35c;
  --ink:#16181c;
  --text:#4a4f57;
  --muted:#8a9099;
  --pale:#f7f8fc;
  --night:#0f1b25;
  --white:#ffffff;
  --line:#d6d9df;
}
*{box-sizing:border-box;margin:0;padding:0}
html,body{width:1200px;height:3440px;overflow:hidden}
body{position:relative;background:var(--white);font-family:"Outfit",sans-serif;color:var(--ink)}
.abs{position:absolute}
a{color:inherit;text-decoration:none}

/* header */
.brand{left:133px;top:22px;display:flex;align-items:center;gap:10px;font-size:24px;font-weight:700;color:var(--green)}
.brand-mark{width:26px;height:26px;background:var(--blue);border-radius:5px}
.nav{left:446px;top:34px;display:flex;gap:34px;font-size:15.5px;font-weight:400}
.nav a.active{border-bottom:2px solid var(--blue);padding-bottom:6px}
.nav-divider{left:895px;top:31px;width:1px;height:26px;background:var(--line)}
.phone-pill{left:923px;top:28px;width:158px;height:34px;border:1.5px solid var(--blue);border-radius:17px;display:flex;align-items:center;justify-content:center;gap:8px;font-size:15px}

/* hero */
.hero-title{left:132px;top:218px;font-size:44px;line-height:51px;font-weight:600;letter-spacing:-.3px}
.hero-sub{left:132px;top:389px;font-size:15.5px;color:var(--ink)}
.btn-pill{left:132px;top:445px;width:142px;height:38px;background:var(--blue);border-radius:19px;color:#fff;font-size:13px;display:flex;align-items:center;justify-content:center;letter-spacing:.2px}
.hero-art{left:574px;top:127px;width:521px;height:467px;border-radius:30px;background:radial-gradient(ellipse at 55% 55%,#e9edf8 0%,#f6f8fd 60%,#fff 100%)}

/* about */
.about-bg{left:0;top:627px;width:1200px;height:640px}
.about-rule{left:163px;top:807px;width:52px;height:4px;background:var(--green)}
.about-title{left:163px;top:826px;font-size:25px;font-weight:500}
.about-text{left:163px;top:866px;width:430px;font-size:14.2px;line-height:24.3px;color:var(--text);font-weight:300}
.btn-outline{left:163px;top:1041px;width:147px;height:40px;border:1.5px solid var(--green);border-radius:20px;display:flex;align-items:center;justify-content:center;font-size:15px;font-weight:500}
.about-circle{left:800px;top:890px;width:300px;height:285px;border-radius:50%;background:#eef0f4}
.about-photo{left:700px;top:765px;width:312px;height:375px;border-radius:24px;background:linear-gradient(160deg,#6f86a6 0%,#b9c4d4 40%,#eceef2 75%,#f6f6f6 100%)}
.badge{left:658px;top:998px;width:140px;height:54px;background:var(--green-soft);border-radius:3px;color:#fff;display:flex;align-items:center;gap:10px;padding-left:14px}
.badge-num{font-size:21px;font-weight:500}
.badge-lbl{font-size:13.5px;line-height:16px;font-weight:300}

/* services */
.services-band{left:0;top:1190px;width:1200px;height:940px}
.services-title{left:0;top:1276px;width:1200px;text-align:center;font-size:48px;font-weight:500;color:#fff}
.services-sub{left:0;top:1347px;width:1200px;text-align:center;font-size:16px;line-height:27px;color:#fff;font-weight:300}
.card{width:273px;height:240px;background:#fff;border-radius:4px;text-align:center}
.card svg{position:absolute;left:50%;top:32px;transform:translateX(-50%)}
.card-title{position:absolute;left:0;right:0;top:122px;font-size:18px;font-weight:500}
.card-text{position:absolute;left:30px;right:30px;top:152px;font-size:11px;line-height:18px;color:var(--muted)}

/* tax */
.tax-bg{left:0;top:2100px;width:1200px;height:592px;background:linear-gradient(115deg,#0e1f1a 0%,#1d3526 40%,#2c4635 65%,#1a2a22 100%)}
.tax-title{left:188px;top:2254px;font-size:32px;line-height:46px;font-weight:600;color:#fff}
.tax-lead{left:188px;top:2360px;width:420px;font-size:19px;line-height:27px;color:#fff;font-weight:400}
.tax-text{left:188px;top:2430px;width:410px;font-size:12.4px;line-height:23px;color:#fff;font-weight:300}
.tax-art{left:681px;top:2229px;width:507px;height:321px;border-radius:50%;background:radial-gradient(circle at 55% 48%,rgba(120,180,200,.35),rgba(40,70,80,.15) 55%,rgba(0,0,0,0) 75%)}

/* contact */
.footer-bg{left:0;top:2985px;width:1200px;height:455px}
.contact-title{left:0;top:2733px;width:1200px;text-align:center;font-size:34px;font-weight:600;letter-spacing:.5px}
.contact-card{left:194px;top:2812px;width:811px;height:302px;background:#fff;border-top:3px solid var(--blue);box-shadow:0 4px 20px rgba(0,0,0,.08)}
.form-title{left:283px;top:2837px;font-size:19px;font-weight:400}
.field{height:30px;border:1px solid var(--line);border-radius:2px;font-size:10.5px;color:var(--muted);padding:8px 14px;font-weight:300}
.btn-submit{left:283px;top:3052px;width:116px;height:32px;background:var(--blue);color:#fff;font-size:12.5px;font-weight:600;display:flex;align-items:center;justify-content:center}

/* footer */
.foot-logo{left:194px;top:3195px;width:166px;height:69px;background:#fff;display:flex;align-items:center;justify-content:center;gap:8px;font-size:20px;font-weight:700;color:var(--green)}
.foot-logo .brand-mark{width:20px;height:20px}
.foot-email{left:194px;top:3300px;display:flex;align-items:center;gap:14px;color:#fff;font-size:11.5px;font-weight:300}
.foot-head{font-size:12.5px;font-weight:600;color:#fff;letter-spacing:.2px}
.foot-rule{height:1px;background:rgba(255,255,255,.25)}
.foot-links{left:577px;top:3230px;display:flex;flex-direction:column;gap:7px;font-size:11.5px;color:#fff;font-weight:300}
.foot-note{left:828px;top:3231px;font-size:11.5px;color:#fff;font-weight:300}
.sub-input{left:828px;top:3255px;width:108px;height:24px;background:#fff}
.sub-btn{left:936px;top:3255px;width:71px;height:24px;background:var(--blue);color:#fff;font-size:10.5px;display:flex;align-items:center;justify-content:center}
.socials{left:828px;top:3302px;display:flex;gap:5px}
.socials span{width:19px;height:19px;border:1px solid #fff;border-radius:50%;display:block}
.copyright{left:184px;top:3397px;font-size:11px;color:#fff;font-weight:300}
.legal{left:847px;top:3397px;font-size:11px;color:#fff;font-weight:300;word-spacing:3px}
</style>
</head>
<body>

<!-- header -->
<div class="abs brand"><span class="brand-mark"></span>Ledgerline</div>
<nav class="abs nav">
  <a class="active" href="#">Home</a><a href="#">About Us</a><a href="#">Services</a><a href="#">Blog</a><a href="#">Contact Us</a>
</nav>
<div class="abs nav-divider"></div>
<div class="abs phone-pill">
  <svg width="14" height="14" viewBox="0 0 24 24"><path fill="#19b2e3" d="M6.6 10.8a15 15 0 0 0 6.6 6.6l2.2-2.2c.3-.3.7-.4 1-.2 1.1.4 2.3.6 3.6.6.6 0 1 .4 1 1V20c0 .6-.4 1-1 1A17 17 0 0 1 3 4c0-.6.4-1 1-1h3.5c.6 0 1 .4 1 1 0 1.3.2 2.5.6 3.6.1.3 0 .7-.2 1z"/></svg>
  0400 123 456
</div>

<!-- hero -->
<h1 class="abs hero-title">We Provide<br>Local Accounting<br>and Bookkeeping</h1>
<p class="abs hero-sub">We Are Calculating The Best Opportunities For You</p>
<a class="abs btn-pill" href="#">LEARN MORE</a>
<div class="abs hero-art" role="img" aria-label="Illustration of an accountant reading reports at a desk while a colleague reviews floating charts"></div>

<!-- about -->
<svg class="abs about-bg" viewBox="0 0 1200 640" preserveAspectRatio="none"><path d="M0 0 Q600 110 1200 0 V640 H0 Z" fill="#f7f8fc"/></svg>
<div class="abs about-rule"></div>
<h2 class="abs about-title">About Us</h2>
<p class="abs about-text">Lorem Ipsum is simply dummy text of the printing and typesetting industry. Lorem Ipsum has been the industry's standard dummy text ever since the 1500s, when an unknown printer took a galley of type and scrambled it to make a type specimen book. It has survived not only five centuries, but also the leap into electronic typesetting, remaining essentially unchanged.</p>
<a class="abs btn-outline" href="#">Learn More</a>
<div class="abs about-circle"></div>
<div class="abs about-photo" role="img" aria-label="Photo of a smiling accountant at her desk in front of office shelves"></div>
<div class="abs badge"><span class="badge-num">10+</span><span class="badge-lbl">Years<br>Experience</span></div>

<!-- services -->
<svg class="abs services-band" viewBox="0 0 1200 940" preserveAspectRatio="none" role="img" aria-label="Green tinted photo of office folders behind the services">
  <defs><linearGradient id="svcGrad" x1="0" y1="0" x2="1" y2="1"><stop offset="0" stop-color="#98c94f"/><stop offset=".5" stop-color="#a9d561"/><stop offset="1" stop-color="#9ccd55"/></linearGradient></defs>
  <path d="M0 98 Q600 -95 1200 98 V852 Q600 1010 0 852 Z" fill="url(#svcGrad)"/>
  <path d="M0 98 Q600 -95 1200 98" fill="none" stroke="#19b2e3" stroke-width="7"/>
  <path d="M0 852 Q600 1010 1200 852" fill="none" stroke="#19b2e3" stroke-width="7"/>
</svg>
<h2 class="abs services-title">Services We Provide</h2>
<p class="abs services-sub">Our business vision is to Plan, Track work to aim to Achieve success and results coordinating<br>support for Industries, Individuals, Organizations that includes.</p>

<div class="abs card" style="left:163px;top:1440px">
  <svg width="70" height="70" viewBox="0 0 70 70"><path d="M12 4h28l12 12v44H12z" fill="none" stroke="#19b2e3" stroke-width="4"/><circle cx="26" cy="22" r="5" fill="#19b2e3"/><rect x="18" y="30" width="16" height="7" rx="3" fill="#19b2e3"/><rect x="40" y="42" width="24" height="16" rx="2" fill="#19b2e3"/><text x="16" y="56" font-size="14" font-weight="700" fill="#19b2e3" font-family="Outfit,sans-serif">$$</text></svg>
  <div class="card-title">PAYROLL</div>
  <p class="card-text">Lorem Ipsum is simply dummy text of the printing and typesetting industry. Lorem Ipsum has been the industry's.</p>
</div>
<div class="abs card" style="left:463px;top:1440px">
  <svg width="70" height="70" viewBox="0 0 70 70"><rect x="6" y="18" width="58" height="34" rx="3" fill="none" stroke="#19b2e3" stroke-width="4"/><rect x="20" y="4" width="30" height="40" fill="#19b2e3"/><g stroke="#fff" stroke-width="2.5"><line x1="25" y1="14" x2="45" y2="14"/><line x1="25" y1="22" x2="45" y2="22"/><line x1="25" y1="30" x2="45" y2="30"/></g><rect x="26" y="56" width="18" height="6" fill="#19b2e3"/></svg>
  <div class="card-title">BOOKKEEPING</div>
  <p class="card-text">Lorem Ipsum is simply dummy text of the printing and typesetting industry. Lorem Ipsum has been the industry's.</p>
</div>
<div class="abs card" style="left:764px;top:1440px">
  <svg width="70" height="70" viewBox="0 0 70 70"><rect x="6" y="6" width="38" height="56" rx="3" fill="#19b2e3"/><g stroke="#fff" stroke-width="3"><line x1="14" y1="44" x2="14" y2="34"/><line x1="21" y1="44" x2="21" y2="28"/><line x1="28" y1="44" x2="28" y2="32"/></g><rect x="40" y="26" width="24" height="36" rx="3" fill="#fff" stroke="#19b2e3" stroke-width="4"/><rect x="45" y="32" width="14" height="7" fill="#19b2e3"/></svg>
  <div class="card-title">ACCONTING</div>
  <p class="card-text">Lorem Ipsum is simply dummy text of the printing and typesetting industry. Lorem Ipsum has been the industry's.</p>
</div>
<div class="abs card" style="left:163px;top:1715px">
  <svg width="70" height="70" viewBox="0 0 70 70"><rect x="22" y="4" width="26" height="20" fill="#19b2e3"/><rect x="20" y="30" width="30" height="34" fill="#19b2e3"/><rect x="10" y="44" width="10" height="20" fill="#19b2e3"/><rect x="50" y="44" width="10" height="20" fill="#19b2e3"/><g stroke="#fff" stroke-width="2.5"><line x1="26" y1="38" x2="44" y2="38"/><line x1="26" y1="46" x2="44" y2="46"/><line x1="26" y1="54" x2="44" y2="54"/></g></svg>
  <div class="card-title">CORPORATE TAX</div>
  <p class="card-text">Lorem Ipsum is simply dummy text of the printing and typesetting industry. Lorem Ipsum has been the industry's.</p>
</div>
<div class="abs card" style="left:463px;top:1715px">
  <svg width="76" height="70" viewBox="0 0 76 70"><rect x="6" y="16" width="60" height="44" rx="4" fill="none" stroke="#19b2e3" stroke-width="4"/><circle cx="24" cy="34" r="6" fill="#19b2e3"/><rect x="15" y="42" width="18" height="10" rx="4" fill="#19b2e3"/><g stroke="#19b2e3" stroke-width="3"><line x1="40" y1="36" x2="58" y2="36"/><line x1="40" y1="46" x2="58" y2="46"/></g><circle cx="64" cy="14" r="10" fill="#19b2e3"/><text x="61" y="19" font-size="12" fill="#fff" font-family="Outfit,sans-serif" font-weight="700">1</text></svg>
  <div class="card-title">PERSONAL TAX</div>
  <p class="card-text">Lorem Ipsum is simply dummy text of the printing and typesetting industry. Lorem Ipsum has been the industry's.</p>
</div>
<div class="abs card" style="left:764px;top:1715px">
  <svg width="70" height="70" viewBox="0 0 70 70"><path d="M10 4h32l12 12v42H10z" fill="#19b2e3"/><text x="17" y="30" font-size="13" font-weight="700" fill="#fff" font-family="Outfit,sans-serif">GST</text><text x="22" y="48" font-size="16" font-weight="700" fill="#fff" font-family="Outfit,sans-serif">%</text><path d="M44 56l6 6 14-14" fill="none" stroke="#19b2e3" stroke-width="4"/></svg>
  <div class="card-title">GST RETURNS</div>
  <p class="card-text">Lorem Ipsum is simply dummy text of the printing and typesetting industry. Lorem Ipsum has been the industry's.</p>
</div>

<!-- tax -->
<div class="abs tax-bg" role="img" aria-label="Dark photo of an open hand under leafy greenery"></div>
<svg class="abs" style="left:0;top:2040px" width="1200" height="90" viewBox="0 0 1200 90" preserveAspectRatio="none"><path d="M0 2 Q600 162 1200 2 V0 H0Z" fill="#9ccd55"/><path d="M0 2 Q600 162 1200 2" fill="none" stroke="#19b2e3" stroke-width="7"/></svg>
<h2 class="abs tax-title">We Will Provide Best Tax<br>Service For Your Business.</h2>
<p class="abs tax-lead">Lorem Ipsum is simply dummy text of the printing and typesetting industry.</p>
<p class="abs tax-text">Lorem Ipsum has been the industry's standard dummy text ever since the 1500s, when an unknown printer took a galley of type and scrambled it to make a type specimen book. It has survived not only five centuries, but also the leap into electronic typesetting, remaining essentially.</p>
<div class="abs tax-art" role="img" aria-label="Illustration of a glowing network globe surrounded by hexagon business icons"></div>

<!-- contact -->
<div class="abs" style="left:0;top:2690px;width:1200px;height:300px;background:#fff"></div>
<svg class="abs footer-bg" viewBox="0 0 1200 455" preserveAspectRatio="none" role="img" aria-label="Dark night landscape photo behind the footer"><path d="M0 20 Q600 -60 1200 20 V455 H0Z" fill="#0f1b25"/></svg>
<h2 class="abs contact-title">CONTACT</h2>
<div class="abs contact-card"></div>
<h3 class="abs form-title">Feel Free to Contact Us</h3>
<div class="abs field" style="left:283px;top:2877px;width:311px">First Name</div>
<div class="abs field" style="left:606px;top:2877px;width:311px">Last Name</div>
<div class="abs field" style="left:283px;top:2921px;width:311px">Email</div>
<div class="abs field" style="left:606px;top:2921px;width:311px">Subject</div>
<div class="abs field" style="left:283px;top:2964px;width:634px;height:73px">Message...</div>
<a class="abs btn-submit" href="#">SUBMIT</a>

<!-- footer -->
<div class="abs foot-logo"><span class="brand-mark"></span>Ledgerline</div>
<div class="abs foot-email">
  <svg width="16" height="14" viewBox="0 0 16 14"><rect x="1" y="4" width="14" height="9" fill="none" stroke="#fff"/><path d="M1 4l7 5 7-5M3 4V1h10v3" fill="none" stroke="#fff"/></svg>
  hello@ledgerline.com
</div>
<div class="abs foot-head" style="left:577px;top:3194px">SITELINKS</div>
<div class="abs foot-rule" style="left:577px;top:3216px;width:157px"></div>
<div class="abs foot-links"><a href="#">Home</a><a href="#">About Us</a><a href="#">Services</a><a href="#">Sitemap</a><a href="#">Contact</a></div>
<div class="abs foot-head" style="left:828px;top:3194px">STAY IN TOUCH</div>
<div class="abs foot-rule" style="left:828px;top:3216px;width:179px"></div>
<div class="abs foot-note">Subscribe Our Newsletter</div>
<div class="abs sub-input"></div>
<div class="abs sub-btn">Subscribe</div>
<div class="abs socials"><span></span><span></span><span></span></div>
<div class="abs foot-rule" style="left:184px;top:3378px;width:832px"></div>
<div class="abs copyright">@2021 Ledgerline Bookkeeping. All Rights Reserved.</div>
<div class="abs legal">Privacy &amp; Policy | Faq | Terms.</div>

</body>
</html>
```